Mining Engineering Services

I would like a 1 page flyer promoting VTR Mining Pty Ltd engineering services using a UAV (Unmanned aerial vehicle). I want something simple yet captures the readers attention. I have a promo video that I would like to attach a hyper link to this brochure. I have four other brochures to make after the successful completion of this one.

Target Market(s)

Mining Industry

Requirements
Must have
• Details from the word doc attached.
• Contact detail to be included;
• Dennis Holloway
• Email - dennis.holloway@vtrmining.example
• Phone - 0418263951

```html
<!DOCTYPE html>
<html lang="en">
<head>
<meta charset="utf-8">
<title>VTR Mining – UAV Engineering Services Flyer</title>
<link href="https://fonts.googleapis.com/css2?family=Montserrat:wght@700;800&family=Lato:wght@400;700&display=swap" rel="stylesheet">
<style>
  :root{
    --brand-blue:#0d57a3;
    --brand-deep:#0a3f80;
    --brand-sky:#3aa3de;
    --panel-grey:#e6e7e9;
    --bar-grey:#5b5c60;
    --text-dark:#222;
    --stage:#3f4042;
  }
  *{box-sizing:border-box;margin:0;padding:0}
  html,body{width:1200px;height:1200px;overflow:hidden;background:var(--stage)}
  .flyer{position:absolute;left:170px;top:0;width:860px;height:1200px;background:#fff;overflow:hidden;font-family:"Lato",sans-serif;color:var(--text-dark)}
  .flyer-art{position:absolute;left:0;top:0;width:860px;height:560px}
  .info-panel{position:absolute;left:488px;top:400px;width:372px;height:775px;background:var(--panel-grey)}
  .bio-box{position:absolute;left:18px;top:543px;width:348px;height:270px;border-radius:0 0 16px 16px;
    background:linear-gradient(180deg,#1e78c4 0%,var(--brand-blue) 45%,var(--brand-deep) 100%);color:#fff;padding:82px 33px 0 19px}
  .bio-title{font-family:"Montserrat",sans-serif;font-weight:800;font-size:16px;letter-spacing:.3px;margin-bottom:14px}
  .bio-text{font-size:11px;line-height:14.3px;text-align:justify;font-weight:700}
  .services-title{position:absolute;left:38px;top:875px;font-family:"Montserrat",sans-serif;font-weight:800;font-size:16px;line-height:20px;color:var(--brand-blue)}
  .services-box{position:absolute;left:27px;top:940px;width:450px;height:202px;background:#eeeff0;display:flex;padding:11px 0 0 8px}
  .services-col{list-style:none;width:215px}
  .services-col + .services-col{border-left:1.5px solid #555;padding-left:18px;height:188px;width:225px}
  .services-col li{display:flex;gap:10px;font-size:12.5px;line-height:15px;margin-bottom:7.5px}
  .tick{flex:none;width:11px;height:11px;margin-top:2px}
  .brand{position:absolute;left:510px;top:600px;width:330px;display:flex;align-items:center;justify-content:center;gap:12px}
  .brand-dot{width:24px;height:24px;border-radius:50%;background:var(--brand-blue)}
  .brand-name{font-family:"Montserrat",sans-serif;font-weight:800;font-size:28px;letter-spacing:4px;color:var(--brand-blue)}
  .uav-title{position:absolute;left:511px;top:697px;font-family:"Montserrat",sans-serif;font-weight:800;font-size:16px;line-height:20px;color:var(--brand-blue)}
  .bullets{position:absolute;list-style:none}
  .bullets li{position:relative;padding-left:17px;font-size:12.5px;line-height:19.7px}
  .bullets li::before{content:"";position:absolute;left:2px;top:8px;width:6px;height:6px;border-radius:50%;background:var(--brand-blue)}
  .uav-list{left:513px;top:785px}
  .sensors-title{position:absolute;left:513px;top:1026px;font-family:"Montserrat",sans-serif;font-weight:800;font-size:16px;color:var(--brand-blue)}
  .sensor-list{left:517px;top:1052px}
  .sensor-list li{font-size:11.5px;font-weight:700;line-height:19.6px}
  .footer-contact{position:absolute;left:0;top:1170px;width:385px;height:30px;border-radius:0 16px 0 0;background:linear-gradient(90deg,var(--brand-deep),#1f7cc8);
    color:#fff;font-size:11px;font-weight:700;display:flex;align-items:center;gap:8px;padding-left:18px;white-space:nowrap}
  .footer-contact a{color:#fff;text-decoration:none}
  .footer-video{position:absolute;left:390px;top:1180px;width:470px;height:20px;background:var(--bar-grey);
    display:flex;align-items:center;justify-content:flex-end;padding-right:20px}
  .footer-video a{color:#fff;font-size:11px;font-weight:700;text-decoration:none;letter-spacing:.3px}
</style>
</head>
<body>
<main class="flyer">
  <div class="info-panel"></div>

  <svg class="flyer-art" viewBox="0 0 860 560">
    <defs>
      <linearGradient id="heroTone" x1="0" y1="0" x2="1" y2="1">
        <stop offset="0" stop-color="#8a7458"/><stop offset=".5" stop-color="#a7916f"/><stop offset="1" stop-color="#6e5a44"/>
      </linearGradient>
      <linearGradient id="pitTone" x1="0" y1="0" x2="0" y2="1">
        <stop offset="0" stop-color="#4aa4e0"/><stop offset=".35" stop-color="#bcd9ee"/><stop offset=".45" stop-color="#c9a45a"/><stop offset="1" stop-color="#7a6a55"/>
      </linearGradient>
      <linearGradient id="roadTone" x1="0" y1="0" x2="1" y2="1">
        <stop offset="0" stop-color="#8a5a3a"/><stop offset=".5" stop-color="#6b4a36"/><stop offset="1" stop-color="#9a6a44"/>
      </linearGradient>
    </defs>
    <path d="M0 0H860V220Q700 440 420 500L0 500Z" fill="#fff"/>
    <path role="img" aria-label="Aerial photo of an open-pit mine with a yellow fixed-wing survey drone in flight" d="M0 0H860V218Q690 420 420 480L0 480Z" fill="url(#heroTone)"/>
    <path d="M860 240Q720 430 470 492" fill="none" stroke="var(--brand-blue)" stroke-width="10"/>
    <path d="M560 486Q470 500 380 508" fill="none" stroke="var(--brand-sky)" stroke-width="6"/>
    <circle cx="158" cy="396" r="184" fill="var(--brand-sky)"/>
    <circle role="img" aria-label="Photo of a drone flying over terraced mine benches under a blue sky" cx="158" cy="396" r="180" fill="url(#pitTone)"/>
    <circle cx="281" cy="473" r="107" fill="var(--brand-deep)"/>
    <circle role="img" aria-label="Aerial photo of haul trucks on a mine road" cx="281" cy="473" r="103" fill="url(#roadTone)"/>
  </svg>

  <section class="bio-box">
    <h2 class="bio-title">COMPANY SHORT BIO</h2>
    <p class="bio-text">VTR Mining Pty Ltd is a Mining Engineering consultancy company with over 15 year's experience in the Mining industry. VTR Mining Pty Ltd provides value adding mining engineering services with the utilisation of industry leading UAV (Unmanned Aerial Vehicle) technology. VTR Mining utilises multiple sensors in the UAV to provide custom solutions to your Mine site. Unlike other UAV survey providers, VTR Mining's engineering expertise can provide assistance from concept to reconciliation of your project.</p>
  </section>

  <h2 class="services-title">SERVICES INCLUDE BUT ARE NOT<br>LIMITED TO</h2>
  <div class="services-box">
    <ul class="services-col">
      <li><svg class="tick" viewBox="0 0 12 12"><circle cx="6" cy="6" r="5" fill="none" stroke="#0d57a3" stroke-width="1.3"/><path d="M3.5 6.2l1.8 1.8 3.4-3.6" fill="none" stroke="#0d57a3" stroke-width="1.3"/></svg><span>Mine operation design and<br>scheduling</span></li>
      <li><svg class="tick" viewBox="0 0 12 12"><circle cx="6" cy="6" r="5" fill="none" stroke="#0d57a3" stroke-width="1.3"/><path d="M3.5 6.2l1.8 1.8 3.4-3.6" fill="none" stroke="#0d57a3" stroke-width="1.3"/></svg><span>Pit optimisation</span></li>
      <li><svg class="tick" viewBox="0 0 12 12"><circle cx="6" cy="6" r="5" fill="none" stroke="#0d57a3" stroke-width="1.3"/><path d="M3.5 6.2l1.8 1.8 3.4-3.6" fill="none" stroke="#0d57a3" stroke-width="1.3"/></svg><span>Rehabilitation design and<br>planning</span></li>
      <li><svg class="tick" viewBox="0 0 12 12"><circle cx="6" cy="6" r="5" fill="none" stroke="#0d57a3" stroke-width="1.3"/><path d="M3.5 6.2l1.8 1.8 3.4-3.6" fill="none" stroke="#0d57a3" stroke-width="1.3"/></svg><span>Surface water drainage</span></li>
      <li><svg class="tick" viewBox="0 0 12 12"><circle cx="6" cy="6" r="5" fill="none" stroke="#0d57a3" stroke-width="1.3"/><path d="M3.5 6.2l1.8 1.8 3.4-3.6" fill="none" stroke="#0d57a3" stroke-width="1.3"/></svg><span>Open pit/stockpile volumes</span></li>
      <li><svg class="tick" viewBox="0 0 12 12"><circle cx="6" cy="6" r="5" fill="none" stroke="#0d57a3" stroke-width="1.3"/><path d="M3.5 6.2l1.8 1.8 3.4-3.6" fill="none" stroke="#0d57a3" stroke-width="1.3"/></svg><span>DEM (Digital Elevation Models)</span></li>
    </ul>
    <ul class="services-col">
      <li><svg class="tick" viewBox="0 0 12 12"><circle cx="6" cy="6" r="5" fill="none" stroke="#0d57a3" stroke-width="1.3"/><path d="M3.5 6.2l1.8 1.8 3.4-3.6" fill="none" stroke="#0d57a3" stroke-width="1.3"/></svg><span>Reconciliation reporting</span></li>
      <li><svg class="tick" viewBox="0 0 12 12"><circle cx="6" cy="6" r="5" fill="none" stroke="#0d57a3" stroke-width="1.3"/><path d="M3.5 6.2l1.8 1.8 3.4-3.6" fill="none" stroke="#0d57a3" stroke-width="1.3"/></svg><span>Thermal imaging for<br>volatile materials</span></li>
      <li><svg class="tick" viewBox="0 0 12 12"><circle cx="6" cy="6" r="5" fill="none" stroke="#0d57a3" stroke-width="1.3"/><path d="M3.5 6.2l1.8 1.8 3.4-3.6" fill="none" stroke="#0d57a3" stroke-width="1.3"/></svg><span>Pit wall inspections</span></li>
      <li><svg class="tick" viewBox="0 0 12 12"><circle cx="6" cy="6" r="5" fill="none" stroke="#0d57a3" stroke-width="1.3"/><path d="M3.5 6.2l1.8 1.8 3.4-3.6" fill="none" stroke="#0d57a3" stroke-width="1.3"/></svg><span>Geo referenced Ortho-mosaics</span></li>
      <li><svg class="tick" viewBox="0 0 12 12"><circle cx="6" cy="6" r="5" fill="none" stroke="#0d57a3" stroke-width="1.3"/><path d="M3.5 6.2l1.8 1.8 3.4-3.6" fill="none" stroke="#0d57a3" stroke-width="1.3"/></svg><span>Site rehabilitation inspections</span></li>
      <li><svg class="tick" viewBox="0 0 12 12"><circle cx="6" cy="6" r="5" fill="none" stroke="#0d57a3" stroke-width="1.3"/><path d="M3.5 6.2l1.8 1.8 3.4-3.6" fill="none" stroke="#0d57a3" stroke-width="1.3"/></svg><span>Multispectral imaging</span></li>
      <li><svg class="tick" viewBox="0 0 12 12"><circle cx="6" cy="6" r="5" fill="none" stroke="#0d57a3" stroke-width="1.3"/><path d="M3.5 6.2l1.8 1.8 3.4-3.6" fill="none" stroke="#0d57a3" stroke-width="1.3"/></svg><span>Surveying services</span></li>
    </ul>
  </div>

  <div class="brand"><span class="brand-dot"></span><span class="brand-name">VTR MINING</span></div>

  <h2 class="uav-title">UAV (Unmanned Aerial Vehicle)<br>information SkyTrace ST200<br>UAV System</h2>
  <ul class="bullets uav-list">
    <li>1.8m wing span</li>
    <li>Fully transportable</li>
    <li>Operates under fully autonomous or manual control</li>
    <li>Highly accurate navigation and positioning systems</li>
    <li>Versatile and flexible operations</li>
    <li>Long flight time + 45min (large surveys per flight)</li>
    <li>Able to operate low rain</li>
    <li>Able to operate in high wind</li>
    <li>Parachute recovery</li>
    <li>Assisted Launch</li>
    <li>Multiple Pod &amp; Sensor Capable</li>
  </ul>

  <h2 class="sensors-title">SENSORS UTILISED</h2>
  <ul class="bullets sensor-list">
    <li>RGB 24 mega pixel camera (Digital Elevation Models)</li>
    <li>Infra-red camera (Thermal imaging)</li>
    <li>NDVI (Multispectral imaging)</li>
    <li>Magnetometer (Magnetic surveys)</li>
  </ul>

  <footer class="footer-contact">
    <span>Dennis Holloway</span><span>|</span>
    <a href="mailto:dennis.holloway@vtrmining.example">dennis.holloway@vtrmining.example</a><span>|</span>
    <a href="tel:0418263951">0418263951</a>
  </footer>
  <div class="footer-video"><a href="#promo-video">▶ Watch our UAV promo video</a></div>
</main>
</body>
</html>
```